Ridgeline Talent Associates Business Card Design

We need a business card design for our new company - Ridgeline Talent Associates. RLTA is a recruitment firm that focuses on recruiting engineers and geologist for mid-size oil and gas companies. We would like our logo on the business card, which is attached, and we would like the color scheme on business cards to coordinate with our logo.

Industry/Entity Type

Oil And Gas

Contact Information for Business Card

Dana Whitlow, Founder and Managing Partner, dmw@ridgelinetalentco.org, 888.507.3942 (work), 5730915.0600 (cell), 573.642.1907 (fax), www.ridgelinetalentco.org

```html
<!DOCTYPE html>
<html lang="en">
<head>
<meta charset="utf-8">
<title>Ridgeline Talent Associates – Business Card</title>
<link rel="stylesheet" href="https://fonts.googleapis.com/css2?family=Cinzel:wght@600&family=Lato:wght@400&display=swap">
<style>
  :root {
    --backdrop: #4a4a4a;
    --card: #ffffff;
    --navy: #1f3578;
    --band: #23428c;
    --ink: #2b2b2b;
    --mark-faint: #e7e8ef;
  }
  * { margin: 0; padding: 0; box-sizing: border-box; }
  html, body { width: 1200px; height: 1000px; overflow: hidden; }
  body { background: var(--backdrop); position: relative; font-family: "Lato", sans-serif; }

  .card { position: absolute; background: var(--card); overflow: hidden; }
  .card--front { left: 190px; top: 136px; width: 601px; height: 351px; }
  .card--back  { left: 460px; top: 520px; width: 603px; height: 353px; }

  /* Front */
  .brand {
    position: absolute; left: 0; right: 0; top: 88px;
    display: flex; flex-direction: column; align-items: center; gap: 18px;
  }
  .brand__dot { width: 84px; height: 84px; border-radius: 50%; background: var(--navy); }
  .brand__name {
    font-family: "Cinzel", serif; font-weight: 600; font-size: 25px;
    color: var(--navy); letter-spacing: 0.5px; white-space: nowrap;
  }

  /* Back */
  .holder { position: absolute; left: 36px; top: 50px; }
  .holder__name {
    font-family: "Cinzel", serif; font-weight: 600; font-size: 19px;
    color: var(--navy); letter-spacing: 0.6px; line-height: 24px;
  }
  .holder__title { font-size: 14px; color: var(--ink); line-height: 20px; }

  .contacts { position: absolute; left: 36px; top: 189px; list-style: none; }
  .contacts li {
    display: flex; align-items: center; gap: 12px;
    font-size: 14px; color: var(--ink); height: 23.3px;
  }
  .contacts svg { width: 16px; height: 16px; fill: var(--navy); flex: none; }

  .watermark {
    position: absolute; left: 320px; top: 70px;
    width: 220px; height: 220px; border-radius: 50%;
    background: var(--mark-faint);
  }
  .band { position: absolute; left: 0; right: 0; bottom: 0; height: 23px; background: var(--band); }
</style>
</head>
<body>

<section class="card card--front">
  <div class="brand">
    <span class="brand__dot"></span>
    <span class="brand__name">Ridgeline Talent Associates</span>
  </div>
</section>

<section class="card card--back">
  <div class="watermark"></div>

  <div class="holder">
    <div class="holder__name">DANA WHITLOW</div>
    <div class="holder__title">Founder &amp; Managing Partner</div>
  </div>

  <ul class="contacts">
    <li>
      <svg viewBox="0 0 16 16" aria-hidden="true"><path d="M3.6 1.2l2.3 2.4-1.2 1.9c.9 2 2.5 3.6 4.5 4.6l1.9-1.2 2.4 2.3-1.3 2.4C7 13.4 2.6 9 1.2 3.2z"/></svg>
      888.507.3942
    </li>
    <li>
      <svg viewBox="0 0 16 16" aria-hidden="true"><path d="M4.5 0.5h7a1 1 0 0 1 1 1v13a1 1 0 0 1-1 1h-7a1 1 0 0 1-1-1v-13a1 1 0 0 1 1-1zm.5 2v10h6v-10zm3 10.6a.8.8 0 1 0 0 1.6.8.8 0 0 0 0-1.6z"/></svg>
      573 0915.0600
    </li>
    <li>
      <svg viewBox="0 0 16 16" aria-hidden="true"><path d="M4 1h8v4H4zM1.5 6h13a1 1 0 0 1 1 1v5h-3v3h-9v-3h-3V7a1 1 0 0 1 1-1zm3.5 4v4h6v-4z"/></svg>
      573.642.1907
    </li>
    <li>
      <svg viewBox="0 0 16 16" aria-hidden="true"><path d="M1 3h14v1.2L8 8.6 1 4.2zm0 2.6l7 4.4 7-4.4V13H1z"/></svg>
      dmw@ridgelinetalentco.org
    </li>
    <li>
      <svg viewBox="0 0 16 16" aria-hidden="true"><path d="M8 .8a7.2 7.2 0 1 0 0 14.4A7.2 7.2 0 0 0 8 .8zm-1 2.1c-.6.9-1.8 1.1-2.2 2.2.6.9 1.8.4 2.3 1.3.3.8-.7 1.4-.3 2.3.5.9 1.5.8 1.6 2 .1.8-.3 1.7.2 2.3A5.6 5.6 0 0 1 2.4 8 5.6 5.6 0 0 1 7 2.9zm3.3.6a5.6 5.6 0 0 1 3.2 6.2c-.7-.3-1.1-1.2-2-1-.9.3-1.6-.5-1.4-1.4.3-.8 1.4-.9 1.3-1.9-.2-.9-1.2-.9-1.1-1.9z"/></svg>
      www.ridgelinetalentco.org
    </li>
  </ul>

  <div class="band"></div>
</section>

</body>
</html>
```